Website Design Request - Management Consulting Firm

We need a Website designed for an IT Management Staffing and Recruiting firm called VENTRIX based in San Francisco.

The firm is an high-end technology staffing agency. Our focus is on quality and high-caliber candidates rather than quantity.

The website will have two main home pages. One for the recruiter and another on for the candidates.

The website needs to optimize for mobile devices as well.

I have attached few mock-ups that I have done just to show what I am thinking. The UI needs to be very clean, fluid, and it needs to have a modern, rustic, professional feel to it.

Target Market(s)

Technology Manager, Director, VP, CIO of Companies that have $4b-10b dollar revenue. Such as oakmeadowhome.example , https://www.lumbervale.example/, tidewell.example, norv.example

Industry/Entity Type

Management Consulting

Number of Pages Required

5+ page

Font styles to use
Sans Serif

Colors
f37122
ffffff

Requirements
Must have
• Please review mock-ups for suggestions
Nice to have
Should not have

```html
<!DOCTYPE html>
<html lang="en">
<head>
<meta charset="utf-8">
<title>VENTRIX – IT Project Management Jobs</title>
<link rel="stylesheet" href="https://fonts.googleapis.com/css2?family=Mulish:wght@400;600;700;800&family=Open+Sans:wght@400;600&display=swap">
<style>
  :root {
    --orange: #f7931e;
    --orange-deep: #f37122;
    --dark: #3b3b3b;
    --ink: #333333;
    --muted: #8a8a8a;
    --white: #ffffff;
    --heading-font: "Mulish", sans-serif;
    --body-font: "Open Sans", sans-serif;
  }
  * { box-sizing: border-box; margin: 0; padding: 0; }
  html, body { width: 1014px; height: 1200px; overflow: hidden; background: var(--white); }
  body { font-family: var(--body-font); color: var(--ink); }
  .page { position: relative; width: 1014px; height: 1200px; }
  .abs { position: absolute; }

  /* Header */
  .site-header { position: absolute; left: 0; top: 0; width: 1014px; height: 74px; border-top: 3px solid var(--orange); background: var(--white); }
  .brand { position: absolute; left: 136px; top: 19px; }
  .brand-name { font-family: var(--heading-font); font-weight: 800; font-size: 27px; letter-spacing: 2px; color: var(--orange-deep); line-height: 1; }
  .brand-tag { font-family: var(--heading-font); font-size: 7px; letter-spacing: .6px; color: var(--ink); margin-top: 4px; text-transform: uppercase; }
  .main-nav a { position: absolute; top: 32px; font-family: var(--heading-font); font-weight: 600; font-size: 11px; color: var(--ink); text-decoration: none; letter-spacing: .3px; }
  .btn-small { position: absolute; top: 26px; height: 24px; font-family: var(--heading-font); font-weight: 700; font-size: 9px; color: var(--white); display: flex; align-items: center; justify-content: center; border-radius: 2px; }
  .btn-signin { left: 756px; width: 56px; background: var(--orange); }
  .btn-signup { left: 820px; width: 58px; background: var(--dark); }

  /* Hero */
  .hero { position: absolute; left: 0; top: 74px; width: 1014px; height: 494px;
    background: radial-gradient(ellipse at 62% 28%, #8a7466 0%, #5f544d 35%, #3f3a37 70%, #2f2c2a 100%); }
  .hero-title { position: absolute; left: 0; width: 1014px; top: 150px; text-align: center; font-family: var(--heading-font); font-weight: 700; font-size: 29px; color: var(--white); }
  .hero-sub { position: absolute; left: 0; width: 1014px; top: 191px; text-align: center; font-family: var(--heading-font); font-weight: 600; font-size: 23px; color: var(--white); }
  .signup-form { position: absolute; left: 170px; top: 239px; width: 674px; height: 46px; background: #1f1f1f; padding: 5px; display: flex; }
  .signup-input { flex: 1; background: var(--white); font-size: 9px; color: var(--ink); display: flex; align-items: center; padding-left: 10px; }
  .signup-btn { width: 136px; background: var(--orange); color: var(--white); font-family: var(--heading-font); font-weight: 800; font-size: 11px; display: flex; align-items: center; justify-content: center; letter-spacing: .3px; }
  .slider-arrow { position: absolute; top: 234px; }
  .hero-employers { position: absolute; left: 0; width: 1014px; top: 393px; text-align: center; font-family: var(--heading-font); font-weight: 700; font-size: 16px; color: var(--white); }
  .hero-employers span { text-decoration: underline; text-underline-offset: 4px; text-decoration-thickness: 1px; }

  /* Tabs */
  .tabs { position: absolute; left: 0; top: 568px; width: 1014px; height: 66px; display: flex; }
  .tab { display: flex; align-items: center; justify-content: center; font-family: var(--heading-font); font-weight: 700; font-size: 16px; color: var(--white); }
  .tab-active { width: 507px; background: var(--orange); position: relative; }
  .tab-active::after { content: ""; position: absolute; left: 306px; bottom: -6px; border-left: 12px solid transparent; border-right: 12px solid transparent; border-top: 6px solid var(--orange); }
  .tab-other { width: 507px; background: var(--dark); }

  /* Steps */
  .eyebrow { position: absolute; left: 0; width: 1014px; top: 676px; text-align: center; font-family: var(--heading-font); font-weight: 700; font-size: 11px; color: var(--muted); }
  .section-title { position: absolute; left: 0; width: 1014px; top: 699px; text-align: center; font-family: var(--heading-font); font-weight: 700; font-size: 17px; color: var(--ink); }
  .devices-visual { position: absolute; left: 136px; top: 766px; width: 338px; height: 215px; border-radius: 6px;
    background: linear-gradient(135deg, #2c3a4a 0%, #5b6470 45%, #cfcfcf 100%); }
  .step-icon { position: absolute; left: 539px; }
  .step-title { position: absolute; left: 614px; font-family: var(--heading-font); font-weight: 700; font-size: 12px; color: var(--ink); }
  .step-text { position: absolute; left: 616px; width: 270px; font-family: var(--heading-font); font-size: 9.5px; line-height: 15px; color: #555; }
  .upload-btn { position: absolute; left: 539px; top: 1021px; width: 155px; height: 29px; background: var(--orange); color: var(--white); font-family: var(--heading-font); font-weight: 800; font-size: 10px; display: flex; align-items: center; justify-content: center; gap: 7px; }

  /* Footer */
  .site-footer { position: absolute; left: 0; top: 1104px; width: 1014px; height: 96px; background: var(--dark); color: var(--white); }
  .follow-label { position: absolute; left: 135px; top: 20px; font-size: 10px; }
  .social { position: absolute; top: 44px; width: 25px; height: 25px; background: #2a2a2a; border-radius: 2px; display: flex; align-items: center; justify-content: center; }
  .social i { width: 7px; height: 7px; background: #cfcfcf; border-radius: 1px; display: block; }
  .footer-nav { position: absolute; right: 136px; top: 30px; font-size: 10.5px; }
  .footer-nav span.sep { margin: 0 6px; }
  .copyright { position: absolute; right: 136px; top: 56px; font-size: 9px; }
</style>
</head>
<body>
<div class="page">

  <header class="site-header">
    <div class="brand">
      <div class="brand-name">VENTRIX</div>
      <div class="brand-tag">Project Management Consulting</div>
    </div>
    <nav class="main-nav">
      <a href="#" style="left:518px">PROFESSIONALS</a>
      <a href="#" style="left:652px">EMPLOYERS</a>
    </nav>
    <div class="btn-small btn-signin">SIGN IN</div>
    <div class="btn-small btn-signup">SIGN UP</div>
  </header>

  <section class="hero" role="img" aria-label="Photo of a smiling woman working at a laptop in a bright office">
    <h1 class="hero-title">Looking for IT Project Managment Jobs?</h1>
    <p class="hero-sub">Upload your Resume accept interview requests get offers</p>
    <div class="signup-form">
      <div class="signup-input">Email Address:</div>
      <div class="signup-btn">GET OFFERS NOW</div>
    </div>
    <svg class="slider-arrow" style="left:24px" width="28" height="28" viewBox="0 0 28 28">
      <circle cx="14" cy="14" r="13" fill="none" stroke="#fff" stroke-width="1.2"/>
      <path d="M16 9 L11 14 L16 19" fill="none" stroke="#fff" stroke-width="1.2"/>
    </svg>
    <svg class="slider-arrow" style="left:963px" width="28" height="28" viewBox="0 0 28 28">
      <circle cx="14" cy="14" r="13" fill="none" stroke="#fff" stroke-width="1.2"/>
      <path d="M12 9 L17 14 L12 19" fill="none" stroke="#fff" stroke-width="1.2"/>
    </svg>
    <p class="hero-employers">Looking for talents? <span>See how it works for Employers</span></p>
  </section>

  <div class="tabs">
    <div class="tab tab-active">How it Works?</div>
    <div class="tab tab-other">Why Us?</div>
  </div>

  <p class="eyebrow">3- SIMPLE STEPS</p>
  <h2 class="section-title">Employers pay 25% more for a better FIT project Manager</h2>

  <div class="devices-visual" role="img" aria-label="Monitor, tablet and phone showing job search screens"></div>

  <svg class="step-icon" style="top:750px" width="62" height="62" viewBox="0 0 62 62">
    <circle cx="31" cy="31" r="29" fill="none" stroke="#f7931e" stroke-width="3"/>
    <path d="M31 2 A29 29 0 0 0 4 22" fill="none" stroke="#3b3b3b" stroke-width="3"/>
    <rect x="21" y="16" width="20" height="27" rx="2" fill="none" stroke="#f7931e" stroke-width="2"/>
    <rect x="25" y="21" width="6" height="6" fill="#f7931e"/>
    <path d="M25 31h12M25 35h12M25 39h9" stroke="#f7931e" stroke-width="1.6"/>
  </svg>
  <div class="step-title" style="top:761px">1. Upload your resume</div>
  <div class="step-text" style="top:783px">Answer few questions and upload your resume.</div>

  <svg class="step-icon" style="top:835px" width="62" height="62" viewBox="0 0 62 62">
    <circle cx="31" cy="31" r="29" fill="none" stroke="#f7931e" stroke-width="3"/>
    <path d="M31 2 A29 29 0 0 1 60 31" fill="none" stroke="#3b3b3b" stroke-width="3"/>
    <circle cx="24" cy="27" r="4" fill="#f7931e"/><rect x="18" y="32" width="12" height="9" rx="2" fill="#f7931e"/>
    <circle cx="38" cy="31" r="4" fill="#f7931e"/><rect x="32" y="36" width="12" height="9" rx="2" fill="#f7931e"/>
    <rect x="26" y="16" width="12" height="7" rx="1" fill="#f7931e"/>
  </svg>
  <div class="step-title" style="top:842px">2. We Send You Interview Requests</div>
  <div class="step-text" style="top:864px">Interested in someone? With a single click, send interview request and let us handle the rest.</div>

  <svg class="step-icon" style="top:922px" width="62" height="62" viewBox="0 0 62 62">
    <circle cx="31" cy="31" r="29" fill="none" stroke="#f7931e" stroke-width="3"/>
    <path d="M31 60 A29 29 0 0 0 60 31" fill="none" stroke="#3b3b3b" stroke-width="3"/>
    <circle cx="27" cy="22" r="6" fill="#f7931e"/>
    <path d="M16 42 Q16 30 27 30 Q33 30 35 34 L35 42 Z" fill="#f7931e"/>
    <rect x="33" y="34" width="14" height="10" rx="1" fill="#f7931e" stroke="#fff" stroke-width="1"/>
  </svg>
  <div class="step-title" style="top:933px">3. Get $1000 Bonus</div>
  <div class="step-text" style="top:955px">Find a job and get $1000 bonus VENTRIX</div>

  <div class="upload-btn">
    <svg width="11" height="11" viewBox="0 0 11 11"><path d="M5.5 1 L2 5 H4.2 V8 H6.8 V5 H9 Z M1 9 H10 V10.5 H1 Z" fill="#fff"/></svg>
    UPLOAD YOUR RESUME
  </div>

  <footer class="site-footer">
    <div class="follow-label">Follow us on social media</div>
    <div class="social" style="left:135px" aria-label="Social network link"><i></i></div>
    <div class="social" style="left:164px" aria-label="Social network link"><i></i></div>
    <div class="social" style="left:193px" aria-label="Social network link"><i></i></div>
    <div class="social" style="left:222px" aria-label="Social network link"><i></i></div>
    <nav class="footer-nav">Home<span class="sep">|</span>About Us<span class="sep">|</span>Jobs<span class="sep">|</span>How It Works<span class="sep">|</span>FAQ’s<span class="sep">|</span>Contact</nav>
    <div class="copyright">© 2016 ventrixtech.example.All Copyrights are Reserved.Privacy | Terms &amp; Conditions</div>
  </footer>

</div>
</body>
</html>
```